Delia Forsby Space Tamer

a larger business card may standard size 4” x 9” describing what I do. I don’t know if this would be considered a flyer. I rearrange, redesign and stage houses for the owner or to sell.

```html
<!DOCTYPE html>
<html lang="en">
<head>
<meta charset="utf-8">
<title>Delia Forsby – Space Tamer Card</title>
<link rel="stylesheet" href="https://fonts.googleapis.com/css2?family=Raleway:ital,wght@0,400;0,500;0,600;0,700;1,600;1,700&display=swap">
<style>
  :root {
    --backdrop: #1c1c1c;
    --paper: #ffffff;
    --rust: #922f20;
    --terracotta: #e88a4e;
    --peach: #f5c8a6;
    --mist: #d7d7d7;
    --rule: #c9c9c9;
  }
  html, body {
    margin: 0;
    padding: 0;
    width: 1189px;
    height: 1200px;
    overflow: hidden;
    background: var(--backdrop);
    font-family: "Raleway", sans-serif;
  }
  .card {
    position: absolute;
    display: block;
    box-shadow: 0 6px 18px rgba(0,0,0,0.5);
  }
  .card-front { left: 169px; top: 195px; width: 851px; height: 379px; }
  .card-back  { left: 168px; top: 609px; width: 854px; height: 379px; }
  .card text { font-family: "Raleway", sans-serif; }
  .fill-paper { fill: var(--paper); }
  .fill-rust { fill: var(--rust); }
  .fill-terracotta { fill: var(--terracotta); }
  .fill-peach { fill: var(--peach); }
  .fill-mist { fill: var(--mist); }
  .name { fill: var(--rust); font-size: 26px; font-weight: 700; }
  .role { fill: var(--rust); font-size: 20px; font-weight: 400; }
  .phone { fill: var(--rust); font-size: 24.5px; font-weight: 700; }
  .email { fill: var(--rust); font-size: 18.5px; font-weight: 400; }
  .tagline { fill: var(--rust); font-size: 15px; font-weight: 600; letter-spacing: 3.5px; }
  .award-lead { fill: var(--rust); font-size: 21px; }
  .award-name { fill: var(--rust); font-size: 21px; font-weight: 700; letter-spacing: 4.5px; }
  .award-title { fill: var(--rust); font-size: 20.5px; letter-spacing: 2px; }
  .address-label { fill: var(--paper); font-size: 17px; font-weight: 700; }
  .address-line { fill: var(--paper); font-size: 17.5px; }
  .praise-lead { fill: var(--rust); font-size: 24.5px; font-weight: 500; letter-spacing: 1px; }
  .praise-quote { fill: var(--rust); font-size: 25px; font-weight: 700; font-style: italic; letter-spacing: 0.5px; }
  .story { fill: var(--rust); font-size: 22px; letter-spacing: 0.5px; }
  .story .emph { font-weight: 700; }
  .motto { fill: var(--paper); font-size: 18.5px; font-weight: 600; letter-spacing: 4.3px; }
  .rule { stroke: var(--rule); stroke-width: 2; }
  .line-rust { stroke: var(--rust); stroke-width: 2; fill: none; }
</style>
</head>
<body>

<svg class="card card-front" viewBox="0 0 1043 465" xmlns="http://www.w3.org/2000/svg">
  <defs>
    <linearGradient id="housePhoto" x1="0" y1="0" x2="0.4" y2="1">
      <stop offset="0" stop-color="#9a7a6a"/>
      <stop offset="0.35" stop-color="#e08a55"/>
      <stop offset="0.75" stop-color="#a8603a"/>
      <stop offset="1" stop-color="#c9b8a8"/>
    </linearGradient>
    <radialGradient id="portraitPhoto" cx="0.5" cy="0.45" r="0.6">
      <stop offset="0" stop-color="#d9a890"/>
      <stop offset="0.6" stop-color="#9c7e70"/>
      <stop offset="1" stop-color="#5a3a2c"/>
    </radialGradient>
  </defs>
  <rect class="fill-paper" width="1043" height="465"/>
  <polygon class="fill-terracotta" points="0,0 303,0 0,201"/>
  <polygon role="img" aria-label="Photo of an adobe-style house with a wooden garage door under desert mountains at dusk" points="330,0 765,0 236,352 0,224" fill="url(#housePhoto)"/>
  <line class="line-rust" x1="781" y1="0" x2="238" y2="361"/>
  <polygon class="fill-peach" points="250,345 463,465 300,465 230,360"/>
  <polygon class="fill-mist" points="295,337 1023,337 1023,465 480,465"/>
  <rect class="fill-rust" x="1023" y="337" width="20" height="128"/>
  <polygon class="fill-terracotta" points="0,215 245,362 385,465 0,465"/>
  <polygon class="fill-rust" points="0,238 325,465 0,465"/>

  <circle cx="896" cy="162" r="114" fill="none" stroke="var(--terracotta)" stroke-width="6"/>
  <path d="M896,48 A114,114 0 0 1 896,276" fill="none" stroke="var(--rust)" stroke-width="6"/>
  <circle role="img" aria-label="Portrait photo of Delia Forsby" cx="896" cy="162" r="110" fill="url(#portraitPhoto)"/>

  <text class="name" x="638" y="193" text-anchor="middle">DELIA FORSBY</text>
  <text class="role" x="638" y="214" text-anchor="middle">Space Tamer</text>
  <line class="rule" x1="512" y1="222" x2="765" y2="222"/>
  <text class="phone" x="638" y="251" text-anchor="middle">503-555-0148</text>
  <text class="email" x="638" y="272" text-anchor="middle">deliaforsby@mailnest.net</text>
  <text class="tagline" x="638" y="300" text-anchor="middle">With little or no cost, delia breathes</text>
  <text class="tagline" x="638" y="320" text-anchor="middle">new life &amp; energy into your home.</text>

  <text class="award-lead" x="692" y="368" text-anchor="middle">As a</text>
  <text class="award-name" x="692" y="402" text-anchor="middle">SUNWARD INTERIORS GUILD</text>
  <text class="award-title" x="692" y="436" text-anchor="middle">NATIONAL AWARD WINNER!</text>

  <text class="address-label" x="29" y="389">Address:</text>
  <text class="address-line" x="29" y="411">4620 W. Calder Lane</text>
  <text class="address-line" x="29" y="433">Yuma, AZ 85365</text>
</svg>

<svg class="card card-back" viewBox="0 0 1046 465" xmlns="http://www.w3.org/2000/svg">
  <rect class="fill-paper" width="1046" height="465"/>
  <polygon class="fill-terracotta" points="214,0 334,0 274,58"/>
  <polygon class="fill-rust" points="707,0 940,0 821,116"/>
  <polygon class="fill-rust" points="0,113 99,212 0,311"/>
  <polygon class="fill-terracotta" points="1046,152 990,207 1046,262"/>
  <polygon class="fill-terracotta" points="134,410 196,348 258,410"/>
  <polygon class="fill-rust" points="812,410 905,318 995,410"/>
  <rect class="fill-terracotta" x="0" y="408" width="1046" height="4"/>
  <rect class="fill-rust" x="0" y="412" width="1046" height="53"/>

  <text class="praise-lead" x="523" y="135" text-anchor="middle">Thrilled Customers Say...</text>
  <text class="praise-quote" x="523" y="165" text-anchor="middle">“ This is just how I dreamed my home would look!”</text>
  <line class="rule" x1="164" y1="188" x2="882" y2="188"/>

  <text class="story" x="523" y="227" text-anchor="middle">For 36 years, Delia was a real estate Broker in Oregon. She has record of</text>
  <text class="story" x="523" y="252" text-anchor="middle">transforming houses that do not sell into homes that sell quickly.</text>
  <text class="story" x="523" y="302" text-anchor="middle">Make your space livable, lovable and <tspan class="emph">profitable...</tspan></text>
  <text class="story" x="523" y="327" text-anchor="middle">...a place where you or your buyer can hardly wait to come home to.</text>
  <text class="story" x="523" y="352" text-anchor="middle">Voila!</text>

  <text class="motto" x="523" y="446" text-anchor="middle">REARRANGED. REDESIGNED. STAGED TO SELL</text>
</svg>

</body>
</html>
```